Create a Brochure Design for Harlow Senior Living

Harlow Senior Living is a subsidiary of the Harlow Care Group. This brochure is specifically for the Harlow Senior Living company and brand. Create a 3 panel, front and back, tri-fold brochure. This brochure will be a way to introduce our senior living care home to the community, prospective, clients, and various referral partners. It is modern and state of the art home. Like the home, the brochure must be eye catching, unique in its deliverables (as it doesn’t feel like a care facility) and demonstrate both attention to detail and comfort. Our organization is sophisticated and built around warmth, care and individualized personal attention. The most important aspect of this design is to focus on creating a nurturing, warm, and inviting feel where you would want to put your own loved ones in our care home.
I am open to the creativity of the designer to develop something based on the above criteria; however I would like the design to work well with the existing collateral material. What I mean by that is that while I want everything to have its own personality and stand out as its own brand representative, I still need to be able to tell that the overall design concept stays stylistically inside of the same ‘family’ of existing designed material. Because of this, below I would like for the designer to pull inspiration from the link to our website (Located below) as well as from the attachment of our recently refreshed business cards (Attached). This should allow each design to be unique and creative, while still staying inside of a framework and the feel/style that I am looking for.
Finally, I want all the designers to understand that this brochure design is for a facility where we are responsible to provide care for active, positive, and happy seniors/elders. We have care professionals and staff on-site to provide 24x7, around the clock, care to the elders and geriatric residents as it is needed and required. The photos that are used must represent aging gracefully and with elegance.
Target Market(s)
Seniors(50+), Caring Family Members, Social Workers, Physicians, Hospitals
Industry/Entity Type
Business
Requirements
Must have
- • The company logo must be included.
Nice to have
- Attached you will find a sampling of images related to the long term care industry. Please feel free to use your own images as you see fit. The interior care home pictures are of our actual facility and should be incorporated into the brochure and your design.
Company Information
• Look under the Harlow Senior Living tab at
www.harlowcaregroup.example.

```html
<!DOCTYPE html>
<html lang="en">
<head>
<meta charset="utf-8">
<title>Harlow Senior Living – Outer Spread</title>
<link rel="stylesheet" href="https://fonts.googleapis.com/css2?family=Cabin:wght@400;500;600&family=Roboto+Slab:wght@700&family=Crimson+Text:wght@600&display=swap">
<style>
  :root {
    --page-bg: #000000;
    --paper: #ffffff;
    --teal-deep: #3f8f8c;
    --teal-mid: #5fb8c4;
    --teal-soft: #bfe4ea;
    --teal-pale: #e4f4f6;
    --aqua-band: #1aa3b8;
    --ink: #3a3a3a;
    --link: #2a5fa8;
    --tagline: #2f5e63;
  }
  * { margin: 0; padding: 0; box-sizing: border-box; }
  html, body { width: 1200px; height: 1017px; overflow: hidden; background: var(--page-bg); }
  .spread {
    position: absolute; left: 44px; top: 116px;
    width: 1111px; height: 785px;
    display: flex; overflow: hidden; background: var(--paper);
    font-family: "Cabin", sans-serif; color: var(--ink);
  }
  .panel { position: relative; width: 370.33px; height: 100%; overflow: hidden; }
  .panel-inside-flap {
    background: linear-gradient(180deg, var(--paper) 0%, var(--paper) 45%, var(--teal-pale) 70%, var(--teal-soft) 100%);
  }
  .panel-back {
    background: linear-gradient(180deg, var(--paper) 0%, var(--paper) 30%, var(--teal-pale) 60%, var(--teal-soft) 100%);
  }
  .panel-cover {
    background: linear-gradient(180deg, #8fd0db 0%, #cdebef 22%, #d9f0f3 45%, #bfe5ea 75%, #a9dbe3 100%);
  }
  .swoosh { position: absolute; left: 0; width: 100%; pointer-events: none; }
  .service { position: absolute; left: 33px; width: 336px; }
  .service h2 {
    font-weight: 500; font-size: 16px; color: var(--teal-deep); margin-bottom: 8px;
  }
  .service p { font-size: 11px; line-height: 2.05; text-align: justify; }
  .service-lifestyle { top: 112px; }
  .service-personal { top: 254px; }
  .photo-bathroom {
    position: absolute; left: 0; bottom: 0; width: 371px; height: 310px;
    background: linear-gradient(180deg, rgba(232,228,212,0) 0%, #e8e2cf 18%, #d9cdb2 55%, #b98f62 100%);
  }
  .contact { position: absolute; top: 295px; left: 0; width: 100%; text-align: center; }
  .brand-name {
    font-family: "Cabin", sans-serif; font-weight: 500; color: var(--teal-deep);
    display: inline-flex; align-items: center; gap: 8px;
  }
  .brand-mark { display: inline-block; background: var(--teal-deep); }
  .contact .brand-name { font-size: 17px; }
  .contact .brand-mark { width: 14px; height: 14px; }
  .contact address { font-style: normal; font-size: 9.5px; line-height: 1.45; margin-top: 30px; color: var(--ink); }
  .contact .see-more { font-size: 9.5px; margin-top: 12px; }
  .contact .web { font-size: 9.5px; color: var(--link); }
  .cover-brand { position: absolute; top: 150px; left: 0; width: 100%; text-align: center; }
  .cover-brand .brand-name { font-size: 30px; }
  .cover-brand .brand-mark { width: 22px; height: 22px; }
  .photo-residence {
    position: absolute; left: 0; top: 288px; width: 100%; height: 210px;
    background: linear-gradient(180deg, #4a9fe0 0%, #9fd0f0 30%, #c97a4a 55%, #a9643c 80%, #6f8f4a 100%);
  }
  .welcome-band { position: absolute; left: 0; top: 450px; width: 100%; height: 230px; }
  .welcome {
    position: absolute; left: 0; top: 465px; width: 100%; text-align: center;
    font-family: "Roboto Slab", serif; font-weight: 700; color: var(--paper);
    transform: rotate(-6deg); line-height: 0.9;
    text-shadow: 2px 3px 3px rgba(0,0,0,0.35);
  }
  .welcome .small { display: block; font-size: 36px; padding-left: 70px; }
  .welcome .large { display: block; font-size: 78px; }
  .tagline {
    position: absolute; left: 0; top: 650px; width: 100%; text-align: center;
    font-family: "Crimson Text", serif; font-weight: 600; font-size: 20px; line-height: 1.35;
    color: var(--tagline);
  }
</style>
</head>
<body>
<main class="spread">
  <section class="panel panel-inside-flap">
    <svg class="swoosh" style="top:0;height:140px" viewBox="0 0 370 140" preserveAspectRatio="none" aria-hidden="true">
      <path d="M0 20 C120 60 260 40 370 10 L370 0 L0 0 Z" fill="var(--teal-pale)"/>
      <path d="M0 40 C140 70 280 45 370 20" stroke="var(--teal-soft)" stroke-width="6" fill="none"/>
    </svg>
    <article class="service service-lifestyle">
      <h2>Lifestyle Support</h2>
      <p>For neighbors who are relatively independent but might benefit from lifestyle support, with assistance as needed, medication management, access to staff 24/7, and regular nursing visits.</p>
    </article>
    <article class="service service-personal">
      <h2>Personal Care</h2>
      <p>Hands-on care: Daily bathing, dressing, toileting, incontinence care, grooming, assistance with ambulation, transfers, range of motion exercises, verbal cueing, medication management, &amp; feeding.</p>
    </article>
    <div class="photo-bathroom" role="img" aria-label="Photo of an accessible resident bathroom with grab bars, towels and a vanity"></div>
  </section>

  <section class="panel panel-back">
    <svg class="swoosh" style="top:0;height:150px" viewBox="0 0 370 150" preserveAspectRatio="none" aria-hidden="true">
      <path d="M0 0 C100 40 160 80 210 150 L0 150 Z" fill="none"/>
      <path d="M0 10 C80 30 130 60 170 120" stroke="var(--teal-pale)" stroke-width="30" fill="none"/>
    </svg>
    <div class="contact">
      <div class="brand-name"><span class="brand-mark"></span>Harlow Senior Living</div>
      <address>42 Harbor View Dr.<br>Seaside, HI 96700<br>808-555-0142</address>
      <p class="see-more">See more at:</p>
      <p class="web">http://www.harlowcaregroup.example/senior-living/our-services/#more-15</p>
    </div>
    <svg class="swoosh" style="bottom:0;height:260px" viewBox="0 0 370 260" preserveAspectRatio="none" aria-hidden="true">
      <path d="M0 120 C120 60 260 90 370 40" stroke="var(--paper)" stroke-width="3" fill="none" opacity="0.8"/>
      <path d="M0 200 C140 140 260 170 370 120" stroke="var(--paper)" stroke-width="4" fill="none" opacity="0.6"/>
    </svg>
  </section>

  <section class="panel panel-cover">
    <svg class="swoosh" style="top:0;height:300px" viewBox="0 0 370 300" preserveAspectRatio="none" aria-hidden="true">
      <path d="M0 60 C120 0 260 20 370 80" stroke="var(--paper)" stroke-width="4" fill="none" opacity="0.7"/>
      <path d="M0 110 C150 40 250 60 370 140" stroke="var(--paper)" stroke-width="2" fill="none" opacity="0.6"/>
      <path d="M0 300 C100 220 250 210 370 250 L370 300 Z" fill="var(--teal-pale)" opacity="0.5"/>
    </svg>
    <div class="cover-brand">
      <div class="brand-name"><span class="brand-mark"></span>Harlow Senior Living</div>
    </div>
    <div class="photo-residence" role="img" aria-label="Photo of the two-storey residence with balcony, stairs and garden under a blue sky"></div>
    <svg class="welcome-band" viewBox="0 0 370 230" preserveAspectRatio="none" aria-hidden="true">
      <path d="M0 80 C120 30 260 20 370 45 L370 160 C260 190 120 200 0 175 Z" fill="var(--aqua-band)"/>
      <path d="M0 175 C120 200 260 190 370 160" stroke="var(--paper)" stroke-width="3" fill="none" opacity="0.7"/>
    </svg>
    <h1 class="welcome"><span class="small">Welcome</span><span class="large">Home!</span></h1>
    <p class="tagline">Quality Care<br>Enrich your Lifestyle</p>
  </section>
</main>
</body>
</html>
```